Tidal Pastry Depot Business card

We are empanada whole-sellers and I want a business card design with a picture of an empanada on it that also mentions first trial order FREE. our contact number 555-274-1193 our website www.zarifaban.com and business email Tomas@zarifaban.com

If you want any of our artwork please feel free to email me at the address above.

```html
<!DOCTYPE html>
<html lang="en">
<head>
<meta charset="utf-8">
<title>Tidal Pastry Depot – Business Card</title>
<link rel="stylesheet" href="https://fonts.googleapis.com/css2?family=Oswald:wght@500;600;700&display=swap">
<style>
  :root {
    --card-yellow: #f8ba2a;
    --ring-orange: #f7941d;
    --ink: #1a1a1a;
    --white: #ffffff;
    --dough-light: #efe6d8;
    --dough-shade: #cbbda8;
  }
  * { margin: 0; padding: 0; box-sizing: border-box; }
  html, body { width: 1200px; height: 685px; overflow: hidden; background: #ffffff; }
  .card {
    position: relative;
    width: 1200px; height: 685px;
    background: var(--card-yellow);
    overflow: hidden;
    font-family: "Oswald", "Arial Narrow", sans-serif;
    color: var(--ink);
  }
  .flower {
    position: absolute;
    border-radius: 50%;
    background: var(--ink);
  }
  .flower--top-left { left: -20px; top: -50px; width: 190px; height: 190px; }
  .flower--top-right { left: 1105px; top: -40px; width: 140px; height: 140px; }
  .flower--bottom-right { left: 1055px; top: 530px; width: 200px; height: 200px; }
  .flower--side { left: 1105px; top: 333px; width: 56px; height: 56px; }
  .flower--ring-bottom { left: 140px; top: 565px; width: 150px; height: 150px; }

  .hero-ring {
    position: absolute;
    left: -140px; top: 53px;
    width: 640px; height: 640px;
    border-radius: 50%;
    background: var(--ring-orange);
  }
  .hero-ring__inner {
    position: absolute;
    left: 24px; top: 24px; right: 24px; bottom: 24px;
    border-radius: 50%;
    background: var(--ink);
  }
  .hero-photo {
    position: absolute;
    left: 14px; top: 14px; right: 14px; bottom: 14px;
    border-radius: 50%;
    background: radial-gradient(circle at 60% 40%, var(--dough-light), var(--dough-shade));
  }
  .promo {
    position: absolute;
    left: 95px; top: 300px;
    width: 330px;
    transform: rotate(-9deg);
    text-align: center;
    font-weight: 700;
    text-transform: uppercase;
    color: var(--ink);
    line-height: 0.95;
    -webkit-text-stroke: 0;
    text-shadow: 3px 0 0 var(--white), -3px 0 0 var(--white), 0 3px 0 var(--white), 0 -3px 0 var(--white),
                 2px 2px 0 var(--white), -2px -2px 0 var(--white), 2px -2px 0 var(--white), -2px 2px 0 var(--white);
  }
  .promo__lead { font-size: 50px; display: block; }
  .promo__mid { font-size: 40px; display: block; }
  .promo__free { font-size: 82px; display: block; }

  .brand {
    position: absolute;
    left: 430px; top: 70px;
    width: 640px;
    text-align: center;
    font-weight: 700;
    font-size: 70px;
    line-height: 1;
    text-transform: uppercase;
    color: var(--ink);
  }
  .brand-rule {
    position: absolute;
    left: 587px; top: 207px;
    width: 290px; height: 3px;
    background: var(--ink);
  }
  .brand-rule::before, .brand-rule::after {
    content: ""; position: absolute; top: -3px;
    width: 9px; height: 9px; border-radius: 50%; background: var(--ink);
  }
  .brand-rule::before { left: -4px; }
  .brand-rule::after { right: -4px; }

  .tagline {
    position: absolute;
    left: 496px; top: 228px;
    font-weight: 600; font-size: 29px;
    letter-spacing: 0.5px;
  }
  .offer {
    position: absolute;
    left: 540px; top: 290px;
    width: 520px;
    text-align: center;
    font-weight: 600;
    text-transform: uppercase;
    line-height: 1.15;
  }
  .offer__line { display: block; font-size: 31px; }
  .offer__price { display: block; font-size: 50px; line-height: 1.1; font-weight: 600; }

  .contact {
    position: absolute;
    left: 560px; top: 455px;
    width: 490px;
    list-style: none;
    text-align: center;
    font-weight: 600;
    font-size: 31px;
    line-height: 46px;
    text-transform: uppercase;
  }
  .contact__item { display: flex; justify-content: center; align-items: center; gap: 10px; }
  .contact__icon { width: 28px; height: 28px; flex: none; }
  .contact__dot { width: 26px; height: 26px; border-radius: 50%; background: var(--ink); flex: none; }
</style>
</head>
<body>
<div class="card">
  <div class="flower flower--top-left" role="img" aria-label="Black flower ornament"></div>
  <div class="flower flower--top-right" role="img" aria-label="Black flower ornament"></div>
  <div class="flower flower--side" role="img" aria-label="Small black flower ornament"></div>
  <div class="flower flower--bottom-right" role="img" aria-label="Black flower ornament"></div>

  <div class="hero-ring">
    <div class="hero-ring__inner">
      <div class="hero-photo" role="img" aria-label="Photo of rows of uncooked crimped curry puffs on a tray"></div>
    </div>
  </div>
  <div class="flower flower--ring-bottom" role="img" aria-label="Black flower ornament"></div>

  <p class="promo">
    <span class="promo__lead">First trial</span>
    <span class="promo__mid">selling<br>the puffs for</span>
    <span class="promo__free">Free</span>
  </p>

  <h1 class="brand">Tidal Pastry Depot</h1>
  <div class="brand-rule"></div>

  <p class="tagline">CURRY PUFF / EMPANADAS</p>

  <p class="offer">
    <span class="offer__line">We sell</span>
    <span class="offer__line">Frozen curry puff with</span>
    <span class="offer__price">Wholesaler price</span>
  </p>

  <ul class="contact">
    <li class="contact__item">
      <svg class="contact__icon" viewBox="0 0 28 28" aria-hidden="true">
        <circle cx="14" cy="14" r="13" fill="#1a1a1a"/>
        <path d="M9.5 7.5l3 0.4 1 3.6-1.8 1.3c0.8 1.8 2 3 3.6 3.8l1.3-1.8 3.6 1 0.4 3c-0.4 1-1.4 1.6-2.6 1.5C11.6 19.8 8.2 16.4 7.9 11c-0.1-1.2 0.6-2.4 1.6-3.5z" fill="#f8ba2a"/>
      </svg>
      555-274-1193
    </li>
    <li class="contact__item"><span class="contact__dot"></span>@zarifaban</li>
    <li class="contact__item">Tomas@zarifaban.com</li>
    <li class="contact__item">www.zarifaban.com</li>
  </ul>
</div>
</body>
</html>
```